Brazilian-Italian food blogger looks for a yummy design for her blog

Ciao everyone! I am looking for a brand new design for my Wordpress food blog, MaRuPAN (marupan.net). The blog is about my deep love with food and with Bologna. I write particularly for the Brazilian crowd.
I talk about gastronomic curiosities of the town, delicious places and specialties that one can only find here. There are also many posts about my trips around Italy.
I would like the new design to be more sophisticated (or should I say professional?), but friendly at the same time.
If possible, I would like to keep its background very clean (if there are patters related to food, like the way it is now, even better), especially because I post many big colourful photos...
Also, since it is a personal blog, I would love if visitors could see a picture of mine and with a short description right at the homepage.
Thank you so much in advance.
Cheers,
Telma.

Target Market(s)

Brazilian people interested in Italian culture and gastronomy.

Colors
fcca95

Requirements
Must have
• A neutral background that does not interfere with photos.
• My photo with a short description on the homepage.
Nice to have
• A background that has something to do with food.
Should not have
• It should not look like a girly blog.

```html
<!DOCTYPE html>
<html lang="en">
<head>
<meta charset="utf-8">
<title>MaRuPAN – My deep love with food</title>
<link href="https://fonts.googleapis.com/css2?family=Questrial&family=Open+Sans:wght@400;600&display=swap" rel="stylesheet">
<style>
:root{
  --brand:#fcca95;
  --nav:#f6c08b;
  --nav-active:#e8a061;
  --accent:#d2782e;
  --accent-dark:#c46d25;
  --text:#555;
  --muted:#777;
  --line:#e3e3e3;
  --rail:#cfcfcf;
  --footer:#2e2e2e;
  --white:#fff;
}
*{box-sizing:border-box;margin:0;padding:0}
html,body{width:1200px;height:2529px;overflow:hidden;background:var(--white)}
body{position:relative;font-family:"Open Sans",Arial,sans-serif;color:var(--text)}
.rail{position:absolute;top:0;height:2428px;width:4px;
  background:repeating-linear-gradient(to bottom,var(--rail) 0 6px,transparent 6px 10px)}
.rail--left{left:160px}.rail--right{left:1038px}

.deco{position:absolute;border-radius:50%}
.deco--garlic{left:10px;top:90px;width:130px;height:180px;background:radial-gradient(circle,#d9a27c 0 30%,#f3e3d8 60%,transparent 70%)}
.deco--chili{left:0;top:520px;width:170px;height:130px;border-radius:40%;background:radial-gradient(ellipse,#c3221a 0 35%,transparent 65%)}
.deco--bay{left:0;top:920px;width:170px;height:240px;background:radial-gradient(ellipse,#6f7b3a 0 40%,transparent 70%)}
.deco--tomato{left:1060px;top:290px;width:150px;height:220px;background:radial-gradient(circle,#c8301f 0 35%,transparent 65%)}
.deco--garlic2{left:1040px;top:840px;width:160px;height:200px;background:radial-gradient(circle,#d49a72 0 30%,#f2e0d2 55%,transparent 70%)}

.logo{position:absolute;left:222px;top:40px;font-family:"Questrial",sans-serif;font-size:38px;color:var(--accent);letter-spacing:1px}
.search{position:absolute;left:782px;top:46px;width:216px;height:30px;border:1px solid #ccc;font-size:12px;color:#888;padding:6px 10px}
.search svg{position:absolute;right:8px;top:8px}

.nav{position:absolute;left:204px;top:101px;width:794px;height:46px;background:var(--nav);display:flex;justify-content:space-between;font-family:"Questrial",sans-serif;font-size:13px;color:var(--white);text-transform:uppercase}
.nav a{flex:none;white-space:nowrap;color:inherit;text-decoration:none;padding:0 16px;line-height:46px}
.nav a.active{background:var(--nav-active)}

.hero{position:absolute;left:204px;top:147px;width:794px;height:364px;background:radial-gradient(ellipse at 50% 45%,#3a4a5c,#18202b 75%)}
.hero-title{position:absolute;top:114px;width:100%;text-align:center;font-family:"Questrial",sans-serif;font-size:38px;color:var(--white);letter-spacing:1px}
.hero-sub{position:absolute;top:178px;width:100%;text-align:center;font-family:"Questrial",sans-serif;font-size:17px;color:var(--white)}
.hero-sub::before,.hero-sub::after{content:"";display:inline-block;width:60px;height:1px;background:#fff;vertical-align:middle;margin:0 12px}
.hero-arrow{position:absolute;top:165px;width:34px;height:34px;border-radius:50%;background:#c9842e;opacity:.85}
.hero-arrow--prev{left:-6px}.hero-arrow--next{right:-6px}
.hero-dots{position:absolute;bottom:14px;width:100%;text-align:center}
.hero-dots span{display:inline-block;width:12px;height:12px;border-radius:50%;background:#bbb;margin:0 2px}
.hero-dots span.on{background:#fff}

.post{position:absolute;left:190px;width:499px;height:422px;border:1px solid var(--line);box-shadow:0 1px 3px rgba(0,0,0,.05)}
.post-title{position:absolute;left:12px;top:22px;font-family:"Questrial",sans-serif;font-size:18px;color:var(--accent);text-transform:uppercase;white-space:nowrap}
.post-photo{position:absolute;left:14px;top:63px;width:457px;height:182px}
.post-text{position:absolute;left:14px;top:260px;width:460px;font-size:11.5px;line-height:21px;color:var(--muted)}
.post-meta{position:absolute;left:14px;top:354px;width:457px;height:36px;border-top:1px solid var(--line);border-bottom:4px solid #111;font-size:11.5px;color:#666;display:flex;align-items:center;padding:0 14px;gap:28px;text-transform:uppercase;white-space:nowrap}
.post-meta .date{margin-left:auto;text-transform:none}
.post-meta span{display:flex;align-items:center;gap:6px}

.pagination{position:absolute;left:508px;top:2381px;display:flex;gap:2px}
.pagination span{width:14px;height:14px;border:1px solid #ccc;background:#f3f3f3;font-size:8px;text-align:center;line-height:12px;color:#999}
.pagination span.on{background:#aaa;color:#fff}
.pagination span.gap{margin-left:10px}

.widget{position:absolute;left:741px;width:269px;border:1px solid var(--line);box-shadow:0 1px 3px rgba(0,0,0,.05)}
.widget-title{font-family:"Questrial",sans-serif;font-size:20px;color:var(--accent);text-transform:uppercase;white-space:nowrap}
.about{top:568px;height:325px;text-align:center}
.about .widget-title{margin-top:18px;font-size:17px}
.about-photo{width:134px;height:134px;border-radius:50%;margin:12px auto 0;background:radial-gradient(circle at 50% 40%,#e8c3a4,#a66b3f 80%)}
.about-text{font-size:11px;line-height:19px;color:var(--muted);margin:24px 28px 0}

.fanbox{top:923px;height:218px;padding:10px 20px}
.fan-head{display:flex;gap:10px;align-items:flex-start}
.fan-name{font-family:"Questrial",sans-serif;color:var(--accent);font-size:16px;margin-top:14px}
.fan-side{font-size:11px;color:#444}
.fan-like{display:inline-block;margin-top:4px;width:44px;height:18px;background:#dfe4ee;border:1px solid #b9c3d6;font-size:10px;color:#3b5998;text-align:center;line-height:16px}
.fan-count{font-size:11px;font-weight:600;color:#333;margin-top:8px}
.fan-grid{display:grid;grid-template-columns:repeat(8,28px);gap:3px;margin-top:6px}
.fan-grid i{display:block;width:28px;height:28px;background:linear-gradient(#c9b39f,#8b6f5c)}
.fan-foot{font-size:10px;color:#333;margin-top:10px;display:flex;align-items:center;gap:6px}
.fan-foot b{display:inline-block;width:11px;height:11px;background:#4a64a0}

.latest{top:1172px;height:335px;padding:20px 14px}
.article{display:flex;gap:12px;margin-top:18px}
.article:first-of-type{margin-top:14px}
.article-thumb{width:80px;height:58px;flex:none;background:linear-gradient(#c98d5a,#6f4a33)}
.article h4{font-family:"Questrial",sans-serif;font-weight:400;font-size:14px;color:var(--accent)}
.article p{font-size:11px;line-height:16px;color:var(--muted)}

.archives{position:absolute;left:741px;top:1542px;width:269px}
.archives .widget-title{font-size:18px;margin-bottom:10px}
.archives li{list-style:none;font-size:12px;color:#666;line-height:31px;padding-left:26px;position:relative}
.archives li::before{content:"›";position:absolute;left:4px;color:#888;font-size:16px}

.photofeed{top:1852px;height:301px;padding:20px 14px}
.feed-grid{display:grid;grid-template-columns:repeat(3,72px);gap:8px;margin:14px 0 0 4px}
.feed-grid i{display:block;width:72px;height:60px}

.newsletter{top:2180px;height:113px;padding:16px 10px}
.newsletter .widget-title{font-size:19px}
.signup{display:flex;margin-top:12px}
.signup input{width:147px;height:30px;border:0;background:#fde3cc;font-family:inherit;font-size:11px;padding:0 8px;color:#b98b66}
.signup button{width:96px;height:30px;border:0;background:var(--accent-dark);color:#fff;font-family:inherit;font-size:12px;text-transform:uppercase}

.footer{position:absolute;left:0;top:2428px;width:1200px;height:101px;background:var(--footer);color:#eee;font-size:12px}
.footer-links{position:absolute;left:208px;top:22px}
.footer-copy{position:absolute;left:208px;top:56px}
.footer-social{position:absolute;left:766px;top:36px;display:flex;gap:16px}
.footer-social i{display:block;width:28px;height:28px}
</style>
</head>
<body>
<div class="rail rail--left"></div>
<div class="rail rail--right"></div>

<div class="deco deco--garlic" role="img" aria-label="Garlic cloves scattered on the page margin"></div>
<div class="deco deco--chili" role="img" aria-label="Red chili peppers"></div>
<div class="deco deco--bay" role="img" aria-label="Dried bay leaves"></div>
<div class="deco deco--tomato" role="img" aria-label="Cherry tomatoes"></div>
<div class="deco deco--garlic2" role="img" aria-label="Garlic cloves"></div>

<header>
  <div class="logo">MaRuPAN</div>
  <div class="search">Search..
    <svg width="12" height="12" viewBox="0 0 12 12"><circle cx="5" cy="5" r="3.8" fill="none" stroke="#777" stroke-width="1.4"/><line x1="8" y1="8" x2="11" y2="11" stroke="#777" stroke-width="1.6"/></svg>
  </div>
  <nav class="nav">
    <a class="active">Home</a><a>I, Telma</a><a>The Blog</a><a>Bella Bo</a><a>Culinary Confessions</a><a>Buoni Posti</a><a>Contact</a>
  </nav>
</header>

<section class="hero" role="img" aria-label="Dark wooden table with bread, herbs, tea and rope, seen from above">
  <div class="hero-title">MY DEEP LOVE WITH FOOD</div>
  <div class="hero-sub">OFFICIAL BLOG PAGE</div>
  <span class="hero-arrow hero-arrow--prev"></span><span class="hero-arrow hero-arrow--next"></span>
  <div class="hero-dots"><span class="on"></span><span></span><span></span><span></span></div>
</section>

<main>
  <article class="post" style="top:572px">
    <h2 class="post-title">Quisque sagittis semper felis, in condimentum</h2>
    <div class="post-photo" role="img" aria-label="Plate of sushi and salmon rolls" style="background:linear-gradient(135deg,#3b2b22,#c9683a 50%,#2d2a26)"></div>
    <p class="post-text">Duis autem vel eum iriure dolor in hendreritvulputate velit esse molestie consequat, vill um dolore eu feugiat nulla facilisis at vero eros accumsan et iusto odio dignissim qui blan dpaesent luptatum zzril delenit augue duisolore te feugait nulla facilisi.</p>
    <div class="post-meta"><span>Read more</span><span>22 Oct</span><span><svg width="12" height="10"><ellipse cx="6" cy="4.5" rx="6" ry="4.5" fill="#555"/></svg>1</span><span><svg width="12" height="11" viewBox="0 0 12 11"><path d="M6 11 0 4.5A3 3 0 0 1 6 1.5 3 3 0 0 1 12 4.5Z" fill="#555"/></svg>34</span><span class="date">15 April 2014</span></div>
  </article>

  <article class="post" style="top:1020px">
    <h2 class="post-title">Quisque sass, in condimentum</h2>
    <div class="post-photo" role="img" aria-label="Seafood stew with lemon in a dark pot" style="background:linear-gradient(135deg,#2a2a2a,#b65a2c 55%,#4a4a48)"></div>
    <p class="post-text">Duis autem vel eum iriure dolor in hendreritvulputate velit esse molestie consequat, vill um dolore eu feugiat nulla facilisis at vero eros accumsan et iusto odio dignissim qui blan dpaesent luptatum zzril delenit augue duisolore te feugait nulla facilisi.</p>
    <div class="post-meta"><span>Read more</span><span>22 Oct</span><span><svg width="12" height="10"><ellipse cx="6" cy="4.5" rx="6" ry="4.5" fill="#555"/></svg>1</span><span><svg width="12" height="11" viewBox="0 0 12 11"><path d="M6 11 0 4.5A3 3 0 0 1 6 1.5 3 3 0 0 1 12 4.5Z" fill="#555"/></svg>34</span><span class="date">15 April 2014</span></div>
  </article>

  <article class="post" style="top:1481px">
    <h2 class="post-title">Quisque sagittis semper felis, in condimentum</h2>
    <div class="post-photo" role="img" aria-label="Filo pastry parcels with basil on a red plate" style="background:linear-gradient(135deg,#7a1010,#e9d9b9 40%,#f5efe4 65%,#8a1414)"></div>
    <p class="post-text">Duis autem vel eum iriure dolor in hendreritvulputate velit esse molestie consequat, vill um dolore eu feugiat nulla facilisis at vero eros accumsan et iusto odio dignissim qui blan dpaesent luptatum zzril delenit augue duisolore te feugait nulla facilisi.</p>
    <div class="post-meta"><span>Read more</span><span>22 Oct</span><span><svg width="12" height="10"><ellipse cx="6" cy="4.5" rx="6" ry="4.5" fill="#555"/></svg>1</span><span><svg width="12" height="11" viewBox="0 0 12 11"><path d="M6 11 0 4.5A3 3 0 0 1 6 1.5 3 3 0 0 1 12 4.5Z" fill="#555"/></svg>34</span><span class="date">15 April 2014</span></div>
  </article>

  <article class="post" style="top:1929px">
    <h2 class="post-title">Quisque sagittis semper felis, in condimentum</h2>
    <div class="post-photo" role="img" aria-label="Shrimp curry with herbs and olives" style="background:linear-gradient(135deg,#d9a21c,#e9b730 45%,#5f7a2a 70%,#c98b15)"></div>
    <p class="post-text">Duis autem vel eum iriure dolor in hendreritvulputate velit esse molestie consequat, vill um dolore eu feugiat nulla facilisis at vero eros accumsan et iusto odio dignissim qui blan dpaesent luptatum zzril delenit augue duisolore te feugait nulla facilisi.</p>
    <div class="post-meta"><span>Read more</span><span>22 Oct</span><span><svg width="12" height="10"><ellipse cx="6" cy="4.5" rx="6" ry="4.5" fill="#555"/></svg>1</span><span><svg width="12" height="11" viewBox="0 0 12 11"><path d="M6 11 0 4.5A3 3 0 0 1 6 1.5 3 3 0 0 1 12 4.5Z" fill="#555"/></svg>34</span><span class="date">15 April 2014</span></div>
  </article>

  <div class="pagination"><span class="on">1</span><span>2</span><span>3</span><span>4</span><span>5</span><span>6</span><span>7</span><span>8</span><span>9</span><span class="gap">»</span></div>
</main>

<aside>
  <section class="widget about">
    <h3 class="widget-title">About me</h3>
    <div class="about-photo" role="img" aria-label="Portrait photo of Telma, the blogger"></div>
    <p class="about-text">Claritas est etiam processus dynamicus, qui sequitur mutationem consuetudium lectorum. Mirum est notare quam littera gothica.</p>
  </section>

  <section class="widget fanbox">
    <div class="fan-head">
      <div class="fan-name">MaRuPAN</div>
      <div class="fan-side">MaRuPAN<br><span class="fan-like">Like</span></div>
    </div>
    <div class="fan-count">30 people likes MaRuPAN</div>
    <div class="fan-grid" role="img" aria-label="Profile pictures of fans">
      <i></i><i></i><i></i><i></i><i></i><i></i><i></i><i></i>
      <i></i><i></i><i></i><i></i><i></i><i></i><i></i><i></i>
    </div>
    <div class="fan-foot"><b></b>PalBook Plugin Login</div>
  </section>

  <section class="widget latest">
    <h3 class="widget-title">Latest articles</h3>
    <div class="article"><div class="article-thumb" role="img" aria-label="Bologna rooftops"></div><div><h4>Nam liber tempoout</h4><p>Typi non habent claritat m; est usius legentis qua.</p></div></div>
    <div class="article"><div class="article-thumb" role="img" aria-label="Bologna porticoes" style="background:linear-gradient(#b5522e,#5a2a1c)"></div><div><h4>Nam liber tempoumt</h4><p>Typi non habent claritatnt m; est usius legentis qua.</p></div></div>
    <div class="article"><div class="article-thumb" role="img" aria-label="Piazza at dusk" style="background:linear-gradient(#4a5f8f,#d08b45)"></div><div><h4>Nam liber tempoului</h4><p>Typi non habent claritatst m; est usius legentis qua.</p></div></div>
  </section>

  <section class="archives">
    <h3 class="widget-title">Archieves</h3>
    <ul>
      <li>January 2013 (123)</li><li>February 2013</li><li>March 2013</li><li>April 2013</li><li>May 2013</li><li>June 2013</li><li>July 2014</li><li>August 2014</li>
    </ul>
  </section>

  <section class="widget photofeed">
    <h3 class="widget-title">Photogram</h3>
    <div class="feed-grid">
      <i role="img" aria-label="Food photo" style="background:linear-gradient(#3a2a1e,#c24a24)"></i>
      <i role="img" aria-label="Food photo" style="background:linear-gradient(#d78a4a,#9a3a1c)"></i>
      <i role="img" aria-label="Food photo" style="background:linear-gradient(#e7c56a,#c9542c)"></i>
      <i role="img" aria-label="Food photo" style="background:linear-gradient(#e9e2d6,#b9573a)"></i>
      <i role="img" aria-label="Food photo" style="background:linear-gradient(#f1ead8,#d8a23a)"></i>
      <i role="img" aria-label="Food photo" style="background:linear-gradient(#c6782e,#6e3a1a)"></i>
      <i role="img" aria-label="City photo" style="background:linear-gradient(#7c5f8a,#a45a3a)"></i>
      <i role="img" aria-label="City photo" style="background:linear-gradient(#6f8fc2,#b0643a)"></i>
      <i role="img" aria-label="City photo" style="background:linear-gradient(#3f6fb0,#c08a4a)"></i>
    </div>
  </section>

  <section class="widget newsletter">
    <h3 class="widget-title">Newsletter signup</h3>
    <div class="signup"><input type="text" placeholder="Email ID"><button>Subscribe</button></div>
  </section>
</aside>

<footer class="footer">
  <div class="footer-links">Terms and Conditions | Privacy Promise | FAQ's | Contact Us</div>
  <div class="footer-copy">Copyright © 2013. All Rights Reserved.</div>
  <div class="footer-social">
    <i style="background:#3b5b9a"></i><i style="background:#2a9fd8"></i><i style="background:#f07a1a"></i><i style="background:#d52a22"></i><i style="background:#b0523e"></i>
  </div>
</footer>
</body>
</html>
```